Women's Clothing / Pip & Tansy's
I'd prefer to have the logo centered at the top of the letterhead and have the address, etc. listed on the bottom. Also, I'm not fond of the little icons that indicate address, phone, email, web. Maybe an envelope with just the logo on the front and the return address on the flap? I think they all look really busy with the big logo in the corner and the address on the bottom. It's something I won't use often, so simple is good.
I really like the front of the business card in #4 and the back of the card in purple. More feedback later on the rest. Thanks for all of the options so far!
Cute design, thanks! What would it look like if the back was purple and the logo was white?

```html
<!DOCTYPE html>
<html lang="en">
<head>
<meta charset="utf-8">
<title>Pip &amp; Tansy's Stationery Set</title>
<link href="https://fonts.googleapis.com/css2?family=Playfair+Display:wght@400&family=Open+Sans:wght@400;600&display=swap" rel="stylesheet">
<style>
  :root{
    --plum:#7b2a6c;
    --gold:#c9862f;
    --paper:#ffffff;
    --bg:#ececec;
    --ink:#5a5a5a;
    --faint:#f3e9f1;
    --rule:#d9d9d9;
  }
  *{box-sizing:border-box;margin:0;padding:0}
  html,body{width:1200px;height:317px;overflow:hidden;background:var(--bg)}
  body{position:relative;font-family:"Open Sans",Arial,sans-serif;color:var(--ink)}
  .piece{position:absolute;background:var(--paper);box-shadow:0 1px 3px rgba(0,0,0,.18);overflow:hidden}
  .brand{display:flex;align-items:center;gap:3px;font-family:"Playfair Display",Georgia,serif;color:var(--plum);white-space:nowrap}
  .brand .dot{border-radius:50%;background:var(--plum);flex:none}
  .brand.light{color:#fff}
  .brand.light .dot{background:#fff}
  .swoosh{position:absolute;top:0;right:0}
  .watermark{position:absolute;border-radius:50%;background:var(--faint)}
  .body-text{position:absolute;font-size:3.1px;line-height:4.4px}
  .body-text p{margin-bottom:3px}
  .footer{position:absolute;left:0;right:0;bottom:6px;text-align:center;font-size:3px;color:var(--ink)}
  .footer::before{content:"";display:block;height:1px;background:var(--plum);margin:0 10px 3px}
  .sig{width:24px;height:6px;border-bottom:1px solid #333;margin:4px 0 2px;border-radius:0 0 50% 20%}
  .seal{position:absolute;border-radius:50%;border:1px solid #8b6f9f}
  .small{font-size:3.4px;line-height:5px}
  .ruled{position:absolute;left:10px;right:10px;top:40px;bottom:14px;background:repeating-linear-gradient(to bottom,transparent 0 7px,var(--rule) 7px 8px)}
  .card.purple{background:var(--plum)}
  .envelope .flap{position:absolute;left:0;top:0;width:100%;height:100%}
</style>
</head>
<body>

<!-- Business cards -->
<div class="piece card" style="left:12px;top:100px;width:86px;height:48px">
  <svg class="swoosh" width="86" height="14" viewBox="0 0 100 16" preserveAspectRatio="none"><path d="M40 0 Q75 3 100 16 V0Z" fill="var(--plum)"/><path d="M40 0 Q75 3 100 16" stroke="var(--gold)" stroke-width="1.2" fill="none"/></svg>
  <div class="brand" style="position:absolute;left:8px;top:18px;font-size:6px"><span class="dot" style="width:8px;height:8px"></span>Pip &amp; Tansy's</div>
  <div class="small" style="position:absolute;left:8px;top:30px;font-size:3px;line-height:4px">Clara Vance, Owner<br>01234 567890</div>
</div>
<div class="piece card" style="left:12px;top:154px;width:86px;height:48px">
  <div class="small" style="position:absolute;left:8px;top:10px;font-size:3px;line-height:4.2px">Clara Vance<br>12 Larkfield Lane, Ashby<br>hello@pipandtansy.com<br>www.pipandtansy.com</div>
  <div class="watermark" style="right:-10px;bottom:-14px;width:40px;height:40px"></div>
</div>
<div class="piece card purple" style="left:12px;top:208px;width:86px;height:48px">
  <div class="brand light" style="position:absolute;left:50%;top:50%;transform:translate(-50%,-50%);font-size:7px"><span class="dot" style="width:9px;height:9px"></span>Pip &amp; Tansy's</div>
</div>
<div class="piece card" style="left:12px;top:262px;width:86px;height:48px">
  <div class="brand" style="position:absolute;left:50%;top:50%;transform:translate(-50%,-50%);font-size:6px"><span class="dot" style="width:8px;height:8px"></span>Pip &amp; Tansy's</div>
</div>

<!-- Letterhead A -->
<div class="piece letterhead" style="left:112px;top:8px;width:170px;height:300px">
  <svg class="swoosh" width="170" height="36" viewBox="0 0 100 20" preserveAspectRatio="none"><path d="M45 0 Q80 4 100 20 V0Z" fill="var(--plum)"/><path d="M45 0 Q80 4 100 20" stroke="var(--gold)" stroke-width=".9" fill="none"/></svg>
  <div class="watermark" style="left:55px;top:120px;width:90px;height:90px"></div>
  <div class="brand" style="position:absolute;left:12px;top:10px;font-size:7px"><span class="dot" style="width:10px;height:10px"></span>Pip &amp; Tansy's</div>
  <div class="body-text" style="left:12px;right:12px;top:44px">
    <p>14 March 2025</p>
    <p>Maren Holt<br>12 Larkfield Lane<br>Ashby, AB1 2CD</p>
    <p>Dear Maren,</p>
    <p>Thank you for choosing our boutique for your seasonal wardrobe. We are delighted to share our newest collection of dresses, blouses and tailored pieces, each chosen with care for comfort, quality and lasting style.</p>
    <p>Our team would love to welcome you in store for a private fitting. Please let us know a date and time that suits you, and we will prepare a selection in your size.</p>
    <p>Thank you for choosing our boutique for your seasonal wardrobe. We are delighted to share our newest collection of dresses, blouses and tailored pieces, each chosen with care for comfort, quality and lasting style.</p>
    <p>We look forward to seeing you soon.</p>
    <p>Kind regards,</p>
    <div class="sig"></div>
    <p>Clara Vance</p>
  </div>
  <div class="seal" style="left:62px;top:232px;width:14px;height:14px"></div>
  <div class="footer">12 Larkfield Lane, Ashby · 01234 567890 · hello@pipandtansy.com</div>
</div>

<!-- Note page -->
<div class="piece notepad" style="left:322px;top:56px;width:114px;height:206px">
  <div class="brand" style="position:absolute;left:50%;top:10px;transform:translateX(-50%);font-size:6px"><span class="dot" style="width:8px;height:8px"></span>Pip &amp; Tansy's</div>
  <div class="ruled"></div>
</div>

<!-- Letterhead B -->
<div class="piece letterhead" style="left:560px;top:8px;width:172px;height:300px">
  <svg class="swoosh" width="172" height="36" viewBox="0 0 100 20" preserveAspectRatio="none"><path d="M45 0 Q80 4 100 20 V0Z" fill="var(--plum)"/><path d="M45 0 Q80 4 100 20" stroke="var(--gold)" stroke-width=".9" fill="none"/></svg>
  <div class="watermark" style="left:58px;top:90px;width:90px;height:90px"></div>
  <div class="brand" style="position:absolute;left:12px;top:10px;font-size:7px"><span class="dot" style="width:10px;height:10px"></span>Pip &amp; Tansy's</div>
  <div class="body-text" style="left:12px;right:12px;top:44px">
    <p>14 March 2025</p>
    <p>Maren Holt<br>12 Larkfield Lane<br>Ashby, AB1 2CD</p>
    <p>Dear Maren,</p>
    <p>Thank you for choosing our boutique for your seasonal wardrobe. We are delighted to share our newest collection of dresses, blouses and tailored pieces, each chosen with care for comfort, quality and lasting style.</p>
    <p>Our team would love to welcome you in store for a private fitting. Please let us know a date and time that suits you, and we will prepare a selection in your size.</p>
    <p>Thank you for choosing our boutique for your seasonal wardrobe. We are delighted to share our newest collection of dresses, blouses and tailored pieces, each chosen with care for comfort, quality and lasting style.</p>
    <p>We look forward to seeing you soon.</p>
    <p>Kind regards,</p>
    <div class="sig"></div>
    <p>Clara Vance</p>
  </div>
  <div class="seal" style="left:64px;top:232px;width:14px;height:14px"></div>
  <div class="footer">12 Larkfield Lane, Ashby · 01234 567890 · hello@pipandtansy.com</div>
</div>

<!-- Compliment cards -->
<div class="piece slip" style="left:752px;top:24px;width:108px;height:70px">
  <svg class="swoosh" width="108" height="16" viewBox="0 0 100 16" preserveAspectRatio="none"><path d="M45 0 Q78 3 100 16 V0Z" fill="var(--plum)"/><path d="M45 0 Q78 3 100 16" stroke="var(--gold)" stroke-width="1" fill="none"/></svg>
  <div class="brand" style="position:absolute;left:8px;top:8px;font-size:6px"><span class="dot" style="width:8px;height:8px"></span>Pip &amp; Tansy's</div>
  <div class="footer" style="bottom:4px;font-size:2.8px">12 Larkfield Lane, Ashby · 01234 567890</div>
</div>
<div class="piece slip" style="left:752px;top:150px;width:112px;height:78px">
  <svg class="swoosh" width="112" height="16" viewBox="0 0 100 16" preserveAspectRatio="none"><path d="M45 0 Q78 3 100 16 V0Z" fill="var(--plum)"/><path d="M45 0 Q78 3 100 16" stroke="var(--gold)" stroke-width="1" fill="none"/></svg>
  <div class="watermark" style="left:40px;top:20px;width:46px;height:46px"></div>
  <div class="brand" style="position:absolute;left:8px;top:8px;font-size:6px"><span class="dot" style="width:8px;height:8px"></span>Pip &amp; Tansy's</div>
  <div class="footer" style="bottom:4px;font-size:2.8px">hello@pipandtansy.com · www.pipandtansy.com</div>
</div>

<!-- Envelopes -->
<div class="piece envelope" style="left:1036px;top:22px;width:154px;height:70px">
  <svg class="flap" viewBox="0 0 154 70" preserveAspectRatio="none"><path d="M0 0 H154 V14 L77 34 L0 14Z" fill="var(--plum)"/></svg>
  <div class="brand light" style="position:absolute;left:50%;top:6px;transform:translateX(-50%);font-size:5px"><span class="dot" style="width:6px;height:6px"></span>Pip &amp; Tansy's</div>
</div>
<div class="piece envelope" style="left:1036px;top:102px;width:154px;height:70px">
  <svg class="flap" viewBox="0 0 154 70" preserveAspectRatio="none"><path d="M0 0 H154 V14 L77 34 L0 14Z" fill="var(--gold)"/></svg>
  <div style="position:absolute;left:0;right:0;top:6px;text-align:center;font-size:3px;color:#fff">12 Larkfield Lane, Ashby, AB1 2CD</div>
</div>
<div class="piece envelope" style="left:1036px;top:182px;width:154px;height:70px">
  <svg class="swoosh" width="154" height="18" viewBox="0 0 100 16" preserveAspectRatio="none"><path d="M50 0 Q80 3 100 16 V0Z" fill="var(--plum)"/><path d="M50 0 Q80 3 100 16" stroke="var(--gold)" stroke-width="1" fill="none"/></svg>
  <div class="brand" style="position:absolute;left:8px;top:8px;font-size:5.5px"><span class="dot" style="width:7px;height:7px"></span>Pip &amp; Tansy's</div>
  <div class="small" style="position:absolute;left:70px;top:38px;font-size:3px;line-height:4px">Maren Holt<br>12 Larkfield Lane<br>Ashby, AB1 2CD</div>
</div>

</body>
</html>
```